Quolvex custom business card design

Need a authentic, innovative business card design for a new mobile app business. I am uploading a few screen images from our app for you to view. I would like app design theme to match business card design. I can also send logo images.

```html
<!DOCTYPE html>
<html lang="en">
<head>
<meta charset="utf-8">
<title>Quolvex Business Card</title>
<link href="https://fonts.googleapis.com/css2?family=Montserrat:wght@400;500;600;800;900&display=swap" rel="stylesheet">
<style>
  :root {
    --bg: #2b2d31;
    --purple: #6b2a9c;
    --purple-soft: #ddd0e6;
    --grey-soft: #d9d9d9;
    --black: #141414;
    --band: #1c1c1c;
    --white: #ffffff;
    --line: #8a8a8a;
    --ink: #111111;
  }
  * { box-sizing: border-box; margin: 0; padding: 0; }
  html, body { width: 1200px; height: 900px; overflow: hidden; }
  body {
    background: var(--bg);
    font-family: "Montserrat", sans-serif;
    position: relative;
  }

  /* Front card */
  .card-front {
    position: absolute;
    left: 210px; top: 140px;
    width: 370px; height: 620px;
    background: var(--purple);
    border-radius: 44px;
    padding: 26px 22px 24px;
  }
  .speaker {
    position: absolute; left: 92px; top: 12px;
    width: 74px; height: 5px; border-radius: 3px;
    background: var(--white);
  }
  .sensor-dots { position: absolute; right: 40px; top: 10px; display: flex; gap: 6px; }
  .sensor-dots span { width: 9px; height: 9px; border-radius: 50%; background: var(--white); }

  .screen {
    position: relative;
    width: 100%; height: 100%;
    background: var(--white);
    border-radius: 30px;
    overflow: hidden;
  }
  .screen-glow {
    position: absolute; left: -40px; top: -60px;
    width: 330px; height: 330px; border-radius: 50%;
    background: linear-gradient(180deg, var(--grey-soft) 0%, var(--grey-soft) 45%, var(--purple-soft) 55%, var(--purple-soft) 100%);
    opacity: .85;
  }
  .brand {
    position: absolute; left: 0; right: 0; top: 40px;
    display: flex; flex-direction: column; align-items: center; gap: 10px;
  }
  .brand-mark {
    width: 96px; height: 96px; border-radius: 50%;
    background: var(--black);
  }
  .brand-name {
    font-weight: 900; font-size: 40px; color: var(--ink); letter-spacing: .5px;
  }

  .name-band {
    position: absolute; left: 0; right: 0; top: 228px;
    height: 92px; background: var(--band);
    display: flex; flex-direction: column; align-items: center; justify-content: center;
  }
  .person-name { color: var(--purple); font-weight: 600; font-size: 27px; letter-spacing: 1px; filter: brightness(1.25); }
  .person-title { color: var(--white); font-weight: 500; font-size: 18px; margin-top: 2px; }

  .contacts {
    position: absolute; left: 30px; right: 30px; top: 340px;
    list-style: none;
  }
  .contact {
    display: flex; flex-direction: column; align-items: center; gap: 6px;
    padding: 10px 0 12px;
    border-bottom: 1.5px solid var(--line);
  }
  .contact:last-child { border-bottom: none; }
  .contact-icon {
    width: 26px; height: 26px; border-radius: 50%;
    background: var(--purple);
    display: flex; align-items: center; justify-content: center;
  }
  .contact-text { font-size: 19px; font-weight: 500; color: var(--ink); }
  .contact-web .contact-text { font-weight: 600; }

  /* Back card */
  .card-back {
    position: absolute;
    left: 630px; top: 140px;
    width: 370px; height: 620px;
    background: var(--black);
    border-radius: 44px;
  }
  .camera {
    position: absolute; left: 26px; top: 30px;
    width: 30px; height: 54px;
    border: 3px solid var(--white); border-radius: 9px;
    display: flex; flex-direction: column; align-items: center; justify-content: space-evenly;
  }
  .camera span { width: 9px; height: 9px; border-radius: 50%; background: var(--white); }
  .camera span:last-child { width: 5px; height: 5px; }
  .back-brand {
    position: absolute; left: 0; right: 0; top: 200px;
    display: flex; flex-direction: column; align-items: center; gap: 18px;
  }
  .back-brand .brand-mark { background: var(--white); width: 110px; height: 110px; }
  .back-brand .brand-name { color: var(--white); font-size: 46px; }
</style>
</head>
<body>

  <article class="card-front" aria-label="Business card front">
    <span class="speaker"></span>
    <div class="sensor-dots"><span></span><span></span></div>
    <div class="screen">
      <div class="screen-glow"></div>
      <div class="brand">
        <div class="brand-mark"></div>
        <div class="brand-name">Quolvex</div>
      </div>
      <div class="name-band">
        <div class="person-name">YOUR NAME</div>
        <div class="person-title">Your Title</div>
      </div>
      <ul class="contacts">
        <li class="contact">
          <span class="contact-icon">
            <svg width="14" height="14" viewBox="0 0 24 24" aria-hidden="true"><path fill="#fff" d="M6.6 10.8a15.1 15.1 0 0 0 6.6 6.6l2.2-2.2c.3-.3.7-.4 1-.2 1.1.4 2.3.6 3.6.6.6 0 1 .4 1 1V20c0 .6-.4 1-1 1A17 17 0 0 1 3 4c0-.6.4-1 1-1h3.5c.6 0 1 .4 1 1 0 1.3.2 2.5.6 3.6.1.3 0 .7-.2 1z"/></svg>
          </span>
          <span class="contact-text">123-456-2100</span>
        </li>
        <li class="contact">
          <span class="contact-icon">
            <svg width="14" height="14" viewBox="0 0 24 24" aria-hidden="true"><rect x="2" y="5" width="20" height="14" rx="2" fill="#fff"/><path d="M3 6l9 7 9-7" fill="none" stroke="#6b2a9c" stroke-width="2"/></svg>
          </span>
          <span class="contact-text">youremail@mailvane.com</span>
        </li>
        <li class="contact contact-web">
          <span class="contact-icon">
            <svg width="15" height="15" viewBox="0 0 24 24" aria-hidden="true"><g fill="none" stroke="#fff" stroke-width="2"><circle cx="12" cy="12" r="9"/><ellipse cx="12" cy="12" rx="4" ry="9"/><path d="M3 12h18"/></g></svg>
          </span>
          <span class="contact-text">www.yourwebsite.com</span>
        </li>
      </ul>
    </div>
  </article>

  <article class="card-back" aria-label="Business card back">
    <div class="camera"><span></span><span></span></div>
    <div class="back-brand">
      <div class="brand-mark"></div>
      <div class="brand-name">Quolvex</div>
    </div>
  </article>

</body>
</html>
```